Brevanta Interiors
Business Card, Stationery Package, Email Signature
Project: Brevanta Interiors
Brevanta Interiors -
Creative Brief
Professional
Marisol Pryde
Managing Director
P.O.Box 4372 Harlow Point, TX 79990 - 4372
mpryde@brevantainteriors.example
www.brevantainteriors.example
Brevanta Interiors is a retail store offering Flooring products and Installation services. We would like to have the following items made: Business Card, Stationery Package (Fax, Letterhead, Envelopes, etc.), and Email Signature. We would like to see two types of fonts created for comparison, the original font and one of your own professional choices. Winner, please provide all design templates for future modification upon completion of the contest. Thank you!
logo, text, slogan, and web address.

```html
<!DOCTYPE html>
<html lang="en">
<head>
<meta charset="utf-8">
<title>Brevanta Interiors – Business Card</title>
<link href="https://fonts.googleapis.com/css2?family=Arimo:ital,wght@0,400;0,700;1,700&display=swap" rel="stylesheet">
<style>
  :root {
    --backdrop: #ecebe8;
    --card: #ffffff;
    --brand-blue: #2b3f93;
    --brand-green: #3c9b3e;
    --ink: #333333;
    --icon: #6a5fb0;
    --divider: #c9c9c9;
  }
  html, body {
    margin: 0;
    width: 1200px;
    height: 780px;
    overflow: hidden;
    background: var(--backdrop);
    font-family: "Arimo", Arial, sans-serif;
  }
  .canvas {
    width: 1200px;
    height: 780px;
    display: flex;
    align-items: center;
    justify-content: center;
  }
  .business-card {
    position: relative;
    width: 900px;
    height: 520px;
    background: var(--card);
    border-radius: 36px;
    box-shadow: 0 8px 26px rgba(0,0,0,0.18);
    box-sizing: border-box;
  }
  .brand {
    position: absolute;
    top: 56px;
    left: 0;
    right: 0;
    text-align: center;
  }
  .brand-mark {
    display: block;
    width: 84px;
    height: 84px;
    margin: 0 auto 12px;
    border-radius: 50%;
    background: var(--brand-green);
  }
  .brand-name {
    margin: 0;
    font-size: 58px;
    font-weight: 700;
    color: var(--brand-blue);
    letter-spacing: -1px;
    line-height: 1;
  }
  .brand-lines {
    position: relative;
    width: 500px;
    height: 48px;
    margin: 6px auto 0;
    white-space: nowrap;
  }
  .brand-services {
    position: absolute;
    left: 0;
    top: 0;
    font-size: 19px;
    letter-spacing: 4px;
    color: var(--brand-green);
    text-transform: uppercase;
  }
  .brand-slogan {
    position: absolute;
    right: 0;
    top: 20px;
    font-size: 20px;
    font-style: italic;
    font-weight: 700;
    color: var(--brand-blue);
  }
  .contact-area {
    position: absolute;
    top: 320px;
    left: 0;
    right: 0;
    display: flex;
    justify-content: center;
  }
  .person {
    width: 300px;
    padding-right: 26px;
    text-align: right;
    border-right: 2px solid var(--divider);
  }
  .person-name {
    margin: 0;
    font-size: 30px;
    font-weight: 700;
    color: var(--brand-blue);
  }
  .person-title {
    margin: 4px 0 12px;
    font-size: 20px;
    font-weight: 700;
    font-style: italic;
    color: var(--brand-green);
  }
  .person-address {
    margin: 0;
    font-size: 20px;
    line-height: 1.35;
    color: var(--ink);
    font-style: normal;
    white-space: nowrap;
  }
  .contact-list {
    list-style: none;
    margin: 0;
    padding: 0 0 0 22px;
    width: 340px;
  }
  .contact-list li {
    display: flex;
    align-items: center;
    gap: 10px;
    font-size: 19px;
    color: var(--ink);
    height: 34px;
    white-space: nowrap;
  }
  .contact-list svg {
    width: 20px;
    height: 20px;
    flex: none;
  }
</style>
</head>
<body>
<main class="canvas">
  <section class="business-card">
    <header class="brand">
      <span class="brand-mark"></span>
      <h1 class="brand-name">Brevanta Interiors</h1>
      <div class="brand-lines">
        <span class="brand-services">Wood · Tile · Carpet</span>
        <span class="brand-slogan">Floors Made Easy</span>
      </div>
    </header>

    <div class="contact-area">
      <div class="person">
        <p class="person-name">Marisol Pryde</p>
        <p class="person-title">Managing Director</p>
        <address class="person-address">P.O.Box 4372<br>Harlow Point, TX 79990 - 4372</address>
      </div>
      <ul class="contact-list">
        <li>
          <svg viewBox="0 0 20 20" aria-hidden="true"><rect x="5" y="1" width="10" height="18" rx="2" fill="var(--icon)"/><rect x="7" y="4" width="6" height="9" fill="#fff"/></svg>
          210.555.0142
        </li>
        <li>
          <svg viewBox="0 0 20 20" aria-hidden="true"><rect x="2" y="8" width="16" height="10" rx="2" fill="var(--icon)"/><path d="M3 8 Q10 1 17 8" stroke="var(--icon)" stroke-width="3" fill="none"/><rect x="7" y="11" width="6" height="4" fill="#fff"/></svg>
          210.555.0187
        </li>
        <li>
          <svg viewBox="0 0 20 20" aria-hidden="true"><circle cx="10" cy="10" r="9" fill="var(--icon)"/><text x="10" y="14.5" font-size="13" font-family="Arial, sans-serif" font-weight="700" text-anchor="middle" fill="#fff">@</text></svg>
          mpryde@brevantainteriors.example
        </li>
        <li>
          <svg viewBox="0 0 20 20" aria-hidden="true"><circle cx="10" cy="10" r="9" fill="var(--icon)"/><g stroke="#fff" stroke-width="1.2" fill="none"><ellipse cx="10" cy="10" rx="4" ry="8"/><line x1="2" y1="10" x2="18" y2="10"/><line x1="10" y1="2" x2="10" y2="18"/></g></svg>
          www.brevantainteriors.example
        </li>
      </ul>
    </div>
  </section>
</main>
</body>
</html>
```